Shampoo and Shower Gel Packaging Design

I need a new packaging design for a men shampoo and shower gel bottle. The packaging must me black (black bottle/package) and the logo should be also monochrom.
For example, black matte bottle and black shiny logo on the packaging (not mandatory).
the design must contain maximum 3 colors.
1. black
2. white (text)
3. grey/dark blue/dark green (colors will be the difference between products parfumes/smell/scences.

Design must be minimalist/elegant/discrete.
Updates

Please check the photos i added for pure inspiration.

Target Market(s)

brand exclusively for MEN - premium clients

Industry/Entity Type

Cosmetics

Font styles to use
Sans Serif

Colors
1b1b1b
5c5c5c
aaaaaa
ffffff
3176b5

Requirements
Must have
• black background
• minimalist design

```html
<!DOCTYPE html>
<html lang="en">
<head>
<meta charset="UTF-8">
<title>Norva Grooming – Body Wash and Shampoo for Men</title>
<link rel="stylesheet" href="https://fonts.googleapis.com/css2?family=Nunito+Sans:wght@300;400&display=swap">
<style>
  :root {
    --backdrop-top: #e9ecef;
    --backdrop-bottom: #f6f8fa;
    --bottle-black: #1b1b1b;
    --seam-grey: #2c2c2c;
    --text-white: #ffffff;
    --scent-blue: #3176b5;
    --scent-grey: #aaaaaa;
    --muted-grey: #5c5c5c;
  }
  * { margin: 0; padding: 0; box-sizing: border-box; }
  html, body {
    width: 1200px;
    height: 857px;
    overflow: hidden;
  }
  body {
    background: linear-gradient(180deg, var(--backdrop-top) 0%, var(--backdrop-bottom) 100%);
    font-family: "Nunito Sans", sans-serif;
    font-weight: 300;
    color: var(--text-white);
    position: relative;
  }
  .bottle {
    position: absolute;
    top: 130px;
    width: 226px;
    height: 520px;
  }
  .bottle--body-wash { left: 324px; }
  .bottle--shampoo { left: 603px; }
  .bottle__shape {
    position: absolute;
    inset: 0;
    width: 226px;
    height: 520px;
  }
  .bottle__body { fill: var(--bottle-black); }
  .bottle__seam { stroke: var(--seam-grey); stroke-width: 1.5; fill: none; }
  .brand {
    position: absolute;
    top: 122px;
    left: 0;
    width: 100%;
    text-align: center;
    font-weight: 300;
    color: var(--text-white);
  }
  .brand__name {
    display: block;
    font-size: 26px;
    letter-spacing: 11px;
    padding-left: 11px;
    line-height: 1;
  }
  .brand__line {
    display: block;
    margin-top: 5px;
    font-size: 6px;
    letter-spacing: 4px;
    padding-left: 4px;
  }
  .scent-mark {
    position: absolute;
    top: 250px;
    left: 93px;
    width: 40px;
    height: 40px;
    border-radius: 50%;
  }
  .scent-mark--blue { background: var(--scent-blue); }
  .scent-mark--grey { background: var(--scent-grey); }
  .product-name {
    position: absolute;
    top: 304px;
    left: 0;
    width: 100%;
    text-align: center;
    font-size: 19px;
    letter-spacing: 1px;
  }
  .product-audience {
    position: absolute;
    top: 344px;
    left: 0;
    width: 100%;
    text-align: center;
    font-size: 12px;
    letter-spacing: 1px;
    font-weight: 400;
  }
</style>
</head>
<body>
  <section class="bottle bottle--body-wash">
    <svg class="bottle__shape" viewBox="0 0 226 520" aria-hidden="true">
      <path class="bottle__body" d="M32,8 Q34,0 44,0 L182,0 Q192,0 194,8 Q226,150 226,300 Q226,430 192,512 Q190,520 180,520 L46,520 Q36,520 34,512 Q0,430 0,300 Q0,150 32,8Z"/>
      <path class="bottle__seam" d="M12,423 L214,423"/>
    </svg>
    <div class="brand"><span class="brand__name">NORVA</span><span class="brand__line">GROOMING</span></div>
    <span class="scent-mark scent-mark--blue"></span>
    <p class="product-name">Body Wash</p>
    <p class="product-audience">FOR MEN</p>
  </section>

  <section class="bottle bottle--shampoo">
    <svg class="bottle__shape" viewBox="0 0 226 520" aria-hidden="true">
      <path class="bottle__body" d="M32,8 Q34,0 44,0 L182,0 Q192,0 194,8 Q226,150 226,300 Q226,430 192,512 Q190,520 180,520 L46,520 Q36,520 34,512 Q0,430 0,300 Q0,150 32,8Z"/>
      <path class="bottle__seam" d="M12,423 L214,423"/>
    </svg>
    <div class="brand"><span class="brand__name">NORVA</span><span class="brand__line">GROOMING</span></div>
    <span class="scent-mark scent-mark--grey"></span>
    <p class="product-name">Shampoo</p>
    <p class="product-audience">FOR MEN</p>
  </section>
</body>
</html>
```